Disease outbreak warning

I need a flyer that explains to hunters how to act as frontline responders to potential disease outbreaks in wildlife populations. In this case the disease is African Swine Fever. We need an at a glance style with plenty of colour and that’s very easy to read.

I HAVE ATTACHED SOME EXISTING FLYERS FROM OVERSEAS ETC THAT CONTAIN SOME OF THE RELEVANT INFO. THEY ARE TO BE USED AS A GUIDE ONLY.
Updates

Need to see some more options. We have some that can be developed successfully but we’d like to see some more options that will suit a national campaign.

Target Market(s)

Australian hunters encountering wild pigs. Typical age is from 18 to 32 but can be older. Male or female.

Colors

Designer to choose colors to be used in the design.

Requirements
Must have
• The KWOTL logo (supplied). It should be relatively small at the bottom of the page. Plus we need room for two or three other logos that can be overprinted on the project if required.
• Must have information for hunters as the main focus.
Nice to have
• A double sided flyer.
Should not have
• US spelling.

```html
<!DOCTYPE html>
<html lang="en">
<head>
<meta charset="utf-8">
<title>African Swine Fever – Hunter Biosecurity Flyer</title>
<link rel="stylesheet" href="https://fonts.googleapis.com/css2?family=Bebas+Neue&family=Oswald:wght@400;500;600;700&family=Archivo+Black&display=swap">
<style>
  :root{
    --red:#e41e26;
    --ink:#1d1d1d;
    --charcoal:#2b2b2b;
    --grey:#8a8a8a;
    --paper:#f4f4f4;
    --white:#ffffff;
    --bg:#e9ecee;
    --head:"Bebas Neue", sans-serif;
    --body:"Oswald", sans-serif;
    --heavy:"Archivo Black", sans-serif;
  }
  *{box-sizing:border-box;margin:0;padding:0}
  html,body{width:1200px;height:1200px;overflow:hidden;background:var(--bg)}
  .canvas{position:relative;width:1200px;height:1200px}
  .spread{position:absolute;left:40px;width:1120px;height:540px;display:flex;background:var(--paper);box-shadow:0 4px 18px rgba(0,0,0,.12)}
  .spread--outside{top:40px}
  .spread--inside{top:620px}
  .panel{position:relative;width:373.33px;height:100%;overflow:hidden;border-right:1px solid #dcdcdc}
  .panel:last-child{border-right:none}
  .caps{font-family:var(--body);text-transform:uppercase;font-weight:600;color:var(--ink);line-height:1.25}
  .red{color:var(--red)}
  .ph{position:absolute}

  /* Precautions panel */
  .precautions{padding:26px 28px}
  .precautions__kicker{font-family:var(--head);font-size:36px;line-height:.9;color:var(--ink)}
  .precautions__title{font-family:var(--head);font-size:64px;line-height:.9;color:var(--red)}
  .precautions__list{list-style:none;margin-top:18px}
  .precautions__item{display:flex;align-items:center;gap:16px;height:58px}
  .precautions__icon{flex:0 0 46px;height:46px;background:var(--red)}
  .precautions__text{font-size:13.5px}

  /* Message panel */
  .message__intro{position:absolute;left:0;top:0;width:100%;height:300px;padding:28px 30px;font-size:15.5px}
  .message__intro p+p{margin-top:6px}
  .pig-icon{left:226px;top:232px;width:84px;height:40px;background:var(--red);border-radius:20px 14px 10px 10px}
  .message__dark{position:absolute;left:0;top:300px;width:100%;height:240px;background:linear-gradient(160deg,#4a4a4a,#222)}
  .message__dark-text{position:absolute;left:30px;top:22px;right:30px;color:var(--white);font-size:15.5px}
  .spread-box{position:absolute;left:24px;right:24px;top:112px;background:var(--red);padding:10px 16px 8px;font-family:var(--head);color:var(--white);line-height:.88}
  .spread-box__small{font-size:36px;color:var(--ink)}
  .spread-box__big{font-size:82px}

  /* Cover panel */
  .cover__photo{left:0;top:0;width:100%;height:260px;background:linear-gradient(180deg,#6f8a5a 0%,#4b4a3a 55%,#3a2f25 100%)}
  .cover__band{left:282px;top:0;width:62px;height:260px;background:linear-gradient(180deg,#a0161b,#6e0e12)}
  .brand{position:absolute;left:22px;top:20px;display:flex;align-items:center;gap:8px;background:rgba(255,255,255,.9);padding:6px 12px 6px 8px;border-radius:24px}
  .brand__dot{width:22px;height:22px;border-radius:50%;background:var(--red)}
  .brand__name{font-family:var(--head);font-size:24px;color:var(--ink);line-height:1}
  .cover__rule{position:absolute;left:0;top:260px;width:100%;height:12px;background:var(--red)}
  .cover__body{position:absolute;left:0;top:272px;width:100%;bottom:0;padding:8px 26px 12px;display:flex;flex-direction:column}
  .cover__kicker{font-family:var(--head);font-size:34px;line-height:.9;color:var(--ink)}
  .cover__kills{font-family:var(--head);font-size:40px;line-height:.9;color:var(--red)}
  .cover__hunters{font-family:var(--head);font-size:60px;line-height:.85;color:var(--red);margin-top:4px}
  .cover__line{font-family:var(--head);font-size:30px;line-height:.9;color:var(--ink)}
  .cover__line--small{font-size:24px}
  .cover__disease{font-family:var(--head);font-size:44px;line-height:.9;color:var(--red)}
  .rifle{right:36px;top:306px;width:18px;height:150px;background:var(--red);border-radius:4px}
  .virus{width:30px;height:30px;border-radius:50%;background:var(--red);opacity:.85}
  .cover__url{margin-top:auto;text-align:center;font-family:var(--body);font-weight:600;letter-spacing:5px;font-size:15px;line-height:1.2;color:var(--ink);border-top:5px solid var(--ink);padding-top:6px}

  /* Inside spread */
  .hunter-photo{left:150px;top:0;width:596px;height:200px;background:linear-gradient(120deg,#7b5a4a 0%,#8fa86a 45%,#5f8a3a 100%);z-index:2}
  .outbreak{padding:210px 26px 0}
  .outbreak__text{font-size:15px}
  .help-box{margin:14px 0 10px;background:var(--red);padding:8px 12px;text-align:center}
  .help-box__small{font-family:var(--body);font-weight:600;text-transform:uppercase;font-size:15px;color:var(--ink)}
  .help-box__big{font-family:var(--head);font-size:40px;line-height:.95;color:var(--white)}
  .outbreak__call{font-size:15px}
  .facts{padding:220px 28px 0}
  .facts__text{font-size:15px}
  .facts__note{font-size:15px;margin-top:20px}
  .gallery{position:absolute;left:18px;top:18px;width:337px;height:250px;display:grid;grid-template-columns:1fr 1fr;grid-template-rows:1fr 1fr;gap:6px}
  .gallery__cell{position:relative}
  .gallery__cell--virus{background:radial-gradient(circle,#444 0%,#9a9a9a 70%,#cfcfcf 100%)}
  .gallery__cell--macro{background:#8cc63f}
  .gallery__cell--pig{background:linear-gradient(160deg,#5b4a4a,#2e2626)}
  .gallery__cell--ear{background:linear-gradient(160deg,#c98a95,#7a3a48)}
  .gallery__label{position:absolute;left:0;right:0;bottom:0;background:var(--red);color:var(--white);font-family:var(--body);font-weight:600;text-transform:uppercase;font-size:11.5px;line-height:1.1;padding:4px 6px;text-align:center}
  .gallery__label--big{font-family:var(--head);font-size:22px}
  .gallery__label--tiny{font-size:8px;font-weight:500}
  .target{position:absolute;left:24px;top:286px;right:24px}
  .target__asf{font-family:var(--heavy);font-size:66px;line-height:.9;color:var(--ink);display:flex;align-items:center;gap:14px;border-bottom:4px solid var(--ink);padding-bottom:4px}
  .target__pig{width:96px;height:44px;background:var(--red);border-radius:24px 16px 10px 10px}
  .target__line{font-family:var(--heavy);font-size:27px;line-height:1.05;text-transform:uppercase}
  .target__line--red{color:var(--red)}
  .target__line--ink{color:var(--ink)}
  .pig-silhouette{right:26px;bottom:18px;width:88px;height:92px;background:var(--grey);border-radius:44px 44px 20px 20px}
</style>
</head>
<body>
<main class="canvas">

  <section class="spread spread--outside">
    <article class="panel precautions">
      <h2 class="precautions__kicker">Respect general</h2>
      <h2 class="precautions__title">Precautions</h2>
      <ul class="precautions__list">
        <li class="precautions__item"><span class="precautions__icon" role="img" aria-label="Icon: boots and cleaning"></span><span class="precautions__text caps">Clean and disinfect your equipment on site</span></li>
        <li class="precautions__item"><span class="precautions__icon" role="img" aria-label="Icon: hunting trophy"></span><span class="precautions__text caps">Clean and disinfect your hunting trophies before leaving the area</span></li>
        <li class="precautions__item"><span class="precautions__icon" role="img" aria-label="Icon: no farm visits"></span><span class="precautions__text caps">Do not visit farms unless it necessary</span></li>
        <li class="precautions__item"><span class="precautions__icon" role="img" aria-label="Icon: dressing area"></span><span class="precautions__text caps">Eviscerate shot wild boar in the designated dressing area of the hunting ground</span></li>
        <li class="precautions__item"><span class="precautions__icon" role="img" aria-label="Icon: no food left for boar"></span><span class="precautions__text caps">Do not leave food for wild boar</span></li>
        <li class="precautions__item"><span class="precautions__icon" role="img" aria-label="Icon: do not share products"></span><span class="precautions__text caps">Do not share home-made products from your hunt or feed them to animals</span></li>
      </ul>
    </article>

    <article class="panel message">
      <div class="message__intro caps">
        <p>African swine fever (ASF) is a highly contagious disease of domestic and wild pigs, it is not a danger to human health but is devastating for farming economy.</p>
        <p class="red">There is no vaccine against it. Lorem ipsum has been the industry's and type setting industry.</p>
      </div>
      <span class="ph pig-icon" role="img" aria-label="Pig icon"></span>
      <div class="message__dark" role="img" aria-label="Dark photo of pigs in the background">
        <p class="message__dark-text caps">As humans, you have both the opportunity to detect cases early and the responsiblity to act appropriately.</p>
        <div class="spread-box">
          <div class="spread-box__small">Don't spread the</div>
          <div class="spread-box__big">Disease</div>
        </div>
      </div>
    </article>

    <article class="panel cover">
      <div class="ph cover__photo" role="img" aria-label="Photo of a shot wild boar lying on the ground"></div>
      <div class="ph cover__band" role="img" aria-label="Red-tinted photo strip"></div>
      <div class="brand"><span class="brand__dot"></span><span class="brand__name">KWOTL</span></div>
      <div class="cover__rule"></div>
      <span class="ph rifle" role="img" aria-label="Red rifle illustration"></span>
      <span class="ph virus" style="left:250px;top:316px" role="img" aria-label="Virus illustration"></span>
      <span class="ph virus" style="left:300px;top:372px;width:20px;height:20px" role="img" aria-label="Virus illustration"></span>
      <div class="cover__body">
        <div class="cover__kicker">African swine fever</div>
        <div class="cover__kills">Kills pigs</div>
        <div class="cover__hunters">Hunters</div>
        <div class="cover__line">Don't be the</div>
        <div class="cover__line cover__line--small">Carrier of a deadly</div>
        <div class="cover__disease">Pig disease</div>
        <div class="cover__url">www.<span class="red">kwotl.org</span>.au</div>
      </div>
    </article>
  </section>

  <section class="spread spread--inside">
    <div class="ph hunter-photo" role="img" aria-label="Photo of a young hunter in camouflage holding a shotgun beside a golden retriever"></div>

    <article class="panel outbreak">
      <p class="outbreak__text caps">An outbreak in Australia would have a significant impact on pig health and production, devastate Australian pork producers. Hunting restrictions could be introduced and entire wild boar population could be wiped out.</p>
      <div class="help-box">
        <div class="help-box__small">You can help protect Australia</div>
        <div class="help-box__big">Against ASF</div>
      </div>
      <p class="outbreak__call caps">You're your eyes and ears in the field. If you see sick or dead pigs, call the emergency animal disease hotline on <span class="red">1800 000 123.</span></p>
    </article>

    <article class="panel facts">
      <p class="facts__text caps">African swing fever (ASF) is a highly contagious disease of both domestic and wild pigs. The Northern Territory government is asking pig hunters to remain vigilant as this serious disease spreads through eastern Europe, China and South East Asia.</p>
      <p class="facts__note caps red">People cannot be infected. ASF can be transmitted through contact between infected animals, clothes or equipment.</p>
    </article>

    <article class="panel target-panel">
      <div class="gallery">
        <div class="gallery__cell gallery__cell--virus" role="img" aria-label="Microscope image of the virus"><span class="gallery__label">African swine fever virus</span></div>
        <div class="gallery__cell gallery__cell--macro" role="img" aria-label="Microscope image of an infected macrophage"><span class="gallery__label">African swine fever infected macrophage</span></div>
        <div class="gallery__cell gallery__cell--pig" role="img" aria-label="Photo of an infected pig"><span class="gallery__label gallery__label--big">Infected pig</span></div>
        <div class="gallery__cell gallery__cell--ear" role="img" aria-label="Photo of a reddened pig ear"><span class="gallery__label gallery__label--tiny">Reddening of the ears is a common sign of African swine fever in pigs.</span></div>
      </div>
      <div class="target">
        <div class="target__asf">ASF <span class="target__pig" role="img" aria-label="Pig icon"></span></div>
        <div class="target__line target__line--red">Hunting?</div>
        <div class="target__line target__line--ink">Make</div>
        <div class="target__line target__line--red">Biosecurity</div>
        <div class="target__line target__line--ink">Your</div>
        <div class="target__line target__line--red">Target.</div>
      </div>
      <span class="ph pig-silhouette" role="img" aria-label="Grey pig silhouette illustration"></span>
    </article>
  </section>

</main>
</body>
</html>
```